Personal Business card and maybe logo or graphic?

I would like a card to give out like you would a business card, however I am not promoting a business, it is just for my personal details.

I have no brand and no logo to worry about.

I would like some images or a logo of some kind or a graphic so the card has some excitement about it.

I am happy if you wish to create a logo/graphic that represents my name, I have seen someone with just their initials as a graphic so for me PH, however I am happy for you to create anything you wish, it does not have to relate to me just make the card look fun and still professional.

Please use the details

Peter Hadley

Ashcombe Lodge
9 The Mews
Fern Close
Bournemouth
Dorset
BH4 2QT

+44 (0)7812 604258
peter@hadleypost.example
linkedin.example/in/hadleypeter

looking for a mix between fun, fresh , young whilst being professional

I am new to this and am looking for you to guide me through the process please ask questions and ideas

I am just tidying up my brief as I am starting to understand more. hope it has not confused anyone
Updates

Reason: I have not had time to review or comment due to personal issues sorry

Hi,

to help would you be so kind as to use these sample details on the card

I am uk based and a few designs have us details which look different

Peter Hadley

Ashcombe lodge

9 The Mews

Fern Close

Bournemouth

Dorset

BH4 2QT

+44 (0)7812 604258

peter@hadleypost.example

many thanks hope that is ok and not too much trouble!

regards

Pim

My are of expertise is IT management / IT Consultancy, incase you wish to incorporate any graphics

My job was that of CIO (Chief Information Officer) or another term is Head of IT

just advising incase this gives any assistance as one designer has asked s may be useful to others

thanks                                   

just thought I have had a look and the UK size for a business card seems to be as per below

I thought I would mention as I guess the US size may be different and other countries too

I found these sizes on Cardforge but guess most companies will be similar

that said maybe you can advise me

I have no idea what cardforge is like so not sure where to get cards made, will figure that out later I guess but I assume dimensions are important for the design

thanks

 

Document Trim Size    

            Horizontal        

        85 x 55 mm           

1004 x 650 pixels           

            Vertical        

        55 x 85 mm           

650 x 1004 pixels           

        Full Bleed Size    

            Horizontal        

        88 x 58 mm           

1039 x 685 pixels           

            Vertical        

        58 x 88 mm           

685 x 1039 pixels           

 many thanks

Target Market(s)

Professional and personal contacts

Industry/Entity Type

Business

```html
<!DOCTYPE html>
<html lang="en">
<head>
<meta charset="utf-8">
<title>Peter Hadley – Business Card</title>
<link rel="stylesheet" href="https://fonts.googleapis.com/css2?family=Open+Sans:wght@400;600;700;800&display=swap">
<style>
  :root {
    --backdrop: #d9d4ce;
    --card: #2a2a2a;
    --card-edge: #1f1f1f;
    --monogram: #d6d6d6;
    --name: #ffffff;
    --detail: #cfcfcf;
    --ray-light: rgba(200, 200, 200, 0.85);
    --ray-mid: rgba(120, 120, 120, 0.45);
    --ray-none: rgba(51, 51, 51, 0);
  }
  * { box-sizing: border-box; margin: 0; padding: 0; }
  html, body {
    width: 1200px;
    height: 800px;
    overflow: hidden;
    background: var(--backdrop);
    font-family: "Open Sans", sans-serif;
  }
  .canvas {
    position: relative;
    width: 1200px;
    height: 800px;
  }
  .card {
    position: absolute;
    top: 232px;
    width: 520px;
    height: 336px;
    background: linear-gradient(160deg, #333333 0%, var(--card) 55%, var(--card-edge) 100%);
    border-radius: 4px;
    overflow: hidden;
    box-shadow: 0 10px 28px rgba(0, 0, 0, 0.28);
  }
  .card--front { left: 60px; }
  .card--back { left: 620px; }

  /* Front face */
  .front-rays {
    position: absolute;
    inset: 0;
    background:
      radial-gradient(ellipse 60% 80% at 62% 60%, rgba(255,255,255,0.10) 0%, rgba(255,255,255,0) 70%),
      radial-gradient(ellipse 40% 55% at 85% 30%, var(--ray-light) 0%, var(--ray-mid) 45%, var(--ray-none) 100%);
    opacity: 0.85;
  }
  .front-monogram {
    position: absolute;
    left: 0;
    right: 0;
    top: 78px;
    text-align: center;
    font-weight: 800;
    font-size: 160px;
    line-height: 1;
    letter-spacing: -4px;
    color: var(--monogram);
  }

  /* Back face */
  .back-rays {
    position: absolute;
    left: 250px;
    top: 40px;
    width: 270px;
    height: 200px;
    background: radial-gradient(ellipse 230px 90px at 40px 110px, var(--ray-light) 0%, var(--ray-mid) 45%, var(--ray-none) 100%);
  }
  .back-monogram {
    position: absolute;
    left: 30px;
    top: 22px;
    font-weight: 800;
    font-size: 66px;
    line-height: 1;
    letter-spacing: -2px;
    color: var(--monogram);
  }
  .holder-name {
    position: absolute;
    left: 30px;
    top: 104px;
    font-weight: 700;
    font-size: 19px;
    color: var(--name);
  }
  .address {
    position: absolute;
    left: 30px;
    top: 160px;
    font-style: normal;
    font-size: 14px;
    line-height: 1.5;
    color: var(--detail);
  }
  .contact {
    position: absolute;
    left: 268px;
    top: 240px;
    list-style: none;
    font-size: 14px;
    line-height: 1.5;
    color: var(--detail);
  }
</style>
</head>
<body>
<main class="canvas">
  <section class="card card--front" aria-label="Card front">
    <div class="front-rays" role="img" aria-label="Grey sunburst rays fanning out behind the monogram"></div>
    <div class="front-monogram">PH</div>
  </section>

  <section class="card card--back" aria-label="Card back">
    <div class="back-rays" role="img" aria-label="Small grey sunburst rays fanning to the right"></div>
    <div class="back-monogram">PH</div>
    <h1 class="holder-name">Peter Hadley</h1>
    <address class="address">
      Ashcombe Lodge, 9 The Mews<br>
      Fern Close, Bournemouth<br>
      Dorset, BH4 2QT
    </address>
    <ul class="contact">
      <li>+44 (0)7812 604258</li>
      <li>peter@hadleypost.example</li>
      <li>linkedin.example/in/hadleypeter</li>
    </ul>
  </section>
</main>
</body>
</html>
```